Veltrium stationery design

Design stationery for us that fits with the colours of the logo. We are looking for letterheads, business cards etc. Something we can use for a prospectus and marketing presentations in power point. Must be completed in such a manner that it represents a corporate image for large enterprise clients and other large organisations. The company is a project assurance and monitoring company that works in all industries.

```html
<!DOCTYPE html>
<html lang="en">
<head>
<meta charset="UTF-8">
<title>Veltrium Business Card</title>
<link href="https://fonts.googleapis.com/css2?family=Montserrat:wght@400;500;700;800&display=swap" rel="stylesheet">
<style>
  :root {
    --backdrop: #1f1f20;
    --brand-blue: #104f9e;
    --navy: #1c3373;
    --orange: #f0652a;
    --red: #e0262b;
    --paper: #ffffff;
    --ink: #444444;
  }
  * { box-sizing: border-box; margin: 0; padding: 0; }
  html, body { width: 1200px; height: 900px; overflow: hidden; }
  body {
    background: var(--backdrop);
    font-family: "Montserrat", sans-serif;
    position: relative;
  }
  .card {
    position: absolute;
    left: 300px;
    width: 600px;
    height: 343px;
    overflow: hidden;
  }
  .card-front { top: 70px; background: var(--brand-blue); }
  .card-back { top: 487px; background: var(--paper); }

  .brand {
    position: absolute;
    display: flex;
    align-items: center;
    gap: 12px;
    font-weight: 800;
    letter-spacing: 1px;
    text-transform: uppercase;
  }
  .brand-dot { border-radius: 50%; flex: none; }
  .card-front .brand { left: 50%; top: 50%; transform: translate(-50%, -50%); font-size: 44px; color: var(--paper); }
  .card-front .brand-dot { width: 44px; height: 44px; background: var(--orange); }
  .card-back .brand { left: 250px; top: 40px; font-size: 30px; color: var(--navy); }
  .card-back .brand-dot { width: 30px; height: 30px; background: var(--orange); }

  .holder { position: absolute; left: 40px; top: 132px; }
  .holder-name { font-size: 22px; font-weight: 700; color: var(--navy); letter-spacing: 0.5px; }
  .holder-role { font-size: 16px; font-weight: 500; color: var(--orange); margin-top: 2px; }
  .rule { position: absolute; left: 118px; right: 40px; top: 168px; height: 1.5px; background: var(--orange); }

  .contacts { position: absolute; left: 40px; top: 202px; list-style: none; }
  .contacts li { display: flex; align-items: center; gap: 9px; font-size: 15px; color: var(--ink); line-height: 23px; }
  .contacts svg { width: 13px; height: 13px; flex: none; }

  .address {
    position: absolute; right: 40px; top: 184px;
    text-align: right; font-size: 15px; line-height: 21px; color: var(--ink);
    font-style: normal;
  }
  .band { position: absolute; left: 0; bottom: 0; width: 600px; height: 36px; }
</style>
</head>
<body>
  <section class="card card-front">
    <div class="brand"><span class="brand-dot"></span>Veltrium</div>
  </section>

  <section class="card card-back">
    <div class="brand"><span class="brand-dot"></span>Veltrium</div>
    <div class="rule"></div>
    <div class="holder">
      <p class="holder-name">JORDAN HALE</p>
      <p class="holder-role">Director</p>
    </div>
    <ul class="contacts">
      <li><svg viewBox="0 0 16 16"><path fill="#f0652a" d="M3.6 1.5l2.3 2.6-1.3 1.9c.9 2 2.4 3.5 4.4 4.4l1.9-1.3 2.6 2.3-1.2 2.5C6.3 13.5 2.5 9.7 1.1 3.7z"/></svg>555-014-2290</li>
      <li><svg viewBox="0 0 16 16"><rect x="1" y="3" width="14" height="10" rx="1" fill="#f0652a"/><path d="M1.5 3.8L8 8.6l6.5-4.8" stroke="#fff" stroke-width="1.3" fill="none"/></svg>info@veltrium.com</li>
      <li><svg viewBox="0 0 16 16"><circle cx="8" cy="8" r="7" fill="#f0652a"/><path d="M1.5 8h13M8 1.2c-2.6 3.8-2.6 9.8 0 13.6M8 1.2c2.6 3.8 2.6 9.8 0 13.6" stroke="#fff" stroke-width="1" fill="none"/></svg>www.veltrium.com</li>
    </ul>
    <address class="address">2150 Meridian Ave<br>Suite 118 Houston,<br>Texas 77024</address>
    <svg class="band" viewBox="0 0 600 36" preserveAspectRatio="none">
      <defs>
        <linearGradient id="band-warm" x1="0" x2="1" y1="0" y2="0">
          <stop offset="0" stop-color="#f0652a"/>
          <stop offset="1" stop-color="#e0262b"/>
        </linearGradient>
      </defs>
      <polygon points="0,0 430,0 418,36 0,36" fill="#104f9e"/>
      <polygon points="430,0 436,0 424,36 418,36" fill="#1c3373"/>
      <polygon points="436,0 600,0 600,36 424,36" fill="url(#band-warm)"/>
    </svg>
  </section>
</body>
</html>
```